Halden Fiber - Fiber Internet to the home postcard

Design a postcard for my company, Halden Fiber, using the logo below. On the front of the card:
- No Buffering • No BS
- Second line should be the logo
- $60 / month • 10-Gigs
- haldenfiber.net

Color palate should follow the colors in the logo.

Address should say
- Special pricing during construction
- Our best price
- Our fastest speed
- $60 / month • 10-Gigs
- haldenfiber.net

Target Market(s)

25 - 55 year olds. Middle income/class. People with kids and pick up trucks

Industry/Entity Type

Fiber Internet Service Provider

Font styles to use
Sans Serif

Colors

Designer to choose colors to be used in the design.

Requirements
Nice to have
• I am open to more creative changes

```html
<!DOCTYPE html>
<html lang="en">
<head>
<meta charset="utf-8">
<title>Halden Fiber – Fiber Postcard</title>
<link href="https://fonts.googleapis.com/css2?family=Montserrat:wght@400;500;600&family=Open+Sans:wght@600;700;800&display=swap" rel="stylesheet">
<style>
  :root{
    --ink:#000000;
    --paper:#ffffff;
    --green:#6cc24a;
    --white:#ffffff;
    --navy:#1b2a5c;
    --stamp:#e6e6e6;
    --rule:#c9c9c9;
    --fiber-dark:#06222a;
    --fiber-mid:#0f6f86;
    --fiber-light:#5fd3e6;
  }
  *{margin:0;padding:0;box-sizing:border-box;}
  html,body{width:1200px;height:2452px;overflow:hidden;}
  body{background:linear-gradient(#a3a3a3,#6f6f6f);position:relative;font-family:"Montserrat",sans-serif;}

  .postcard{position:absolute;left:176px;width:656px;height:436px;transform-origin:0 0;transform:scale(1.2);overflow:hidden;box-shadow:0 2px 6px rgba(0,0,0,.35);}
  .postcard--front{top:1226px;background:var(--ink);}
  .postcard--back{top:1794px;background:var(--paper);}

  /* Front */
  .fiber-photo{position:absolute;left:0;top:0;width:440px;height:436px;
    background:radial-gradient(ellipse at 35% 45%,var(--fiber-light) 0%,var(--fiber-mid) 35%,var(--fiber-dark) 70%,var(--ink) 100%);}
  .front-panel{position:absolute;left:400px;top:0;width:248px;height:436px;text-align:center;color:var(--white);font-family:"Open Sans",sans-serif;}
  .headline{position:absolute;top:30px;left:0;width:100%;font-size:70px;font-weight:800;line-height:80px;color:var(--green);letter-spacing:-1px;}
  .headline-sub{position:absolute;top:112px;left:0;width:100%;font-size:23px;font-weight:800;letter-spacing:.5px;}
  .brand{position:absolute;top:188px;left:0;width:100%;text-align:center;}
  .brand-name{font-size:32px;font-weight:700;color:var(--white);white-space:nowrap;}

  .offer{position:absolute;width:188px;height:88px;border:2px solid var(--green);border-radius:6px;display:flex;align-items:center;font-family:"Open Sans",sans-serif;color:var(--white);}
  .offer-cell{flex:1;text-align:center;line-height:1;}
  .offer-cell + .offer-cell{border-left:2px solid var(--green);height:62px;display:flex;flex-direction:column;justify-content:center;flex:0 0 76px;}
  .offer-value{font-size:34px;font-weight:800;color:var(--green);display:block;}
  .offer-unit{font-size:20px;font-weight:600;display:block;margin-top:2px;}
  .offer-unit--small{font-size:16px;font-family:"Montserrat",sans-serif;font-weight:500;}
  .front-panel .offer{left:30px;top:283px;}
  .web{position:absolute;left:0;width:100%;text-align:center;font-family:"Open Sans",sans-serif;font-weight:600;font-size:21px;color:var(--white);}
  .front-panel .web{top:387px;}

  /* Back */
  .back-panel{position:absolute;left:0;top:0;width:328px;height:436px;background:var(--ink);text-align:center;color:var(--white);}
  .promo-kicker{position:absolute;top:36px;width:100%;font-size:21px;font-weight:500;color:var(--green);}
  .promo-sub{position:absolute;top:62px;width:100%;font-size:20px;font-weight:500;}
  .promo-our{position:absolute;top:110px;width:100%;font-size:48px;font-weight:500;line-height:1;}
  .promo-points{position:absolute;top:164px;width:100%;font-size:19px;font-weight:500;color:var(--green);line-height:22px;}
  .back-panel .offer{left:70px;top:253px;}
  .back-panel .web{top:386px;}

  .stamp{position:absolute;left:545px;top:34px;width:78px;height:78px;background:var(--stamp);}
  .address-line{position:absolute;left:371px;width:252px;height:1px;background:var(--rule);}
  .back-brand{position:absolute;right:33px;top:380px;}
  .back-brand .brand-name{font-family:"Open Sans",sans-serif;font-size:20px;font-weight:700;color:var(--navy);}
</style>
</head>
<body>
  <section class="postcard postcard--front">
    <div class="fiber-photo" role="img" aria-label="Glowing blue fiber optic strands with network cable plugs"></div>
    <div class="front-panel">
      <div class="headline">NO BS</div>
      <div class="headline-sub">BUFFERING</div>
      <div class="brand"><span class="brand-name">Halden Fiber</span></div>
      <div class="offer">
        <div class="offer-cell"><span class="offer-value">$60</span><span class="offer-unit">month</span></div>
        <div class="offer-cell"><span class="offer-value">10</span><span class="offer-unit offer-unit--small">GIGS</span></div>
      </div>
      <div class="web">haldenfiber.net</div>
    </div>
  </section>

  <section class="postcard postcard--back">
    <div class="back-panel">
      <div class="promo-kicker">SPECIAL PRICING</div>
      <div class="promo-sub">during construction</div>
      <div class="promo-our">OUR</div>
      <div class="promo-points">FASTEST SPEED<br>BEST PRICE</div>
      <div class="offer">
        <div class="offer-cell"><span class="offer-value">$60</span><span class="offer-unit">month</span></div>
        <div class="offer-cell"><span class="offer-value">10</span><span class="offer-unit offer-unit--small">GIGS</span></div>
      </div>
      <div class="web">haldenfiber.net</div>
    </div>
    <div class="stamp"></div>
    <div class="address-line" style="top:190px"></div>
    <div class="address-line" style="top:245px"></div>
    <div class="address-line" style="top:300px"></div>
    <div class="back-brand"><span class="brand-name">Halden Fiber</span></div>
  </section>
</body>
</html>
```